R Vandell tile

This add will be posted on a shopping cart at grocery store. I have limited space and need something to tie in all my info.Add will be top to bottom not horizontal
R. Vandell
Custom Tile & Marble
"4 generations of Service"
Our slogan is: creating the most beautiful living spaces
555-284-7160
www.vandelltile.example
email:rkhome19@mailbox.example
in business since 1975
We would like to use the color yellow in the design and R. Vandell has to be script font to match our trucks.

Target Market(s)

tile & marble flooring,walls, complete bathroom renovations new homes,remodels,

Industry/Entity Type

Shopping

Colors
ffc214
000000
b1b1b1
f37123

Requirements
Must have
• Would like yellow to be used sparingly all other colors are just a suggestion. Need R. Vandell To be in Script all other wording to be straight
Nice to have
• all contact info,other colors to tie into yellow

```html
<!DOCTYPE html>
<html lang="en">
<head>
<meta charset="utf-8">
<title>R. Vandell Custom Tile &amp; Marble</title>
<link rel="stylesheet" href="https://fonts.googleapis.com/css2?family=Courgette&family=Arimo:wght@400;500&display=swap">
<style>
  :root {
    --yellow: #ffc214;
    --black: #000000;
    --grey: #b1b1b1;
    --orange: #f37123;
    --paper: #ffffff;
  }
  html, body {
    margin: 0;
    padding: 0;
    overflow: hidden;
    background: var(--paper);
  }
  .canvas {
    position: relative;
    width: 1200px;
    height: 848px;
    background: var(--paper);
    font-family: "Arimo", Arial, sans-serif;
    color: var(--black);
    overflow: hidden;
  }
  .accent-bars {
    position: absolute;
    left: 0;
    top: 0;
  }
  .line {
    position: absolute;
    left: 386px;
    width: 400px;
    text-align: center;
    line-height: 1;
    white-space: nowrap;
    margin: 0;
  }
  .brand-name {
    top: 186px;
    left: 345px;
    width: 500px;
    font-family: "Courgette", cursive;
    font-size: 60px;
    letter-spacing: 2px;
  }
  .trade {
    top: 271px;
    left: 385px;
    font-size: 24px;
    letter-spacing: 0.5px;
  }
  .motto {
    top: 298px;
    left: 396px;
    font-size: 16px;
    letter-spacing: 0.6px;
  }
  .established {
    top: 362px;
    left: 394px;
    font-size: 16px;
    letter-spacing: 0.6px;
  }
  .phone {
    top: 397px;
    left: 388px;
    font-size: 24px;
    color: var(--yellow);
    letter-spacing: 1px;
    font-weight: 500;
  }
  .website {
    top: 423px;
    left: 393px;
    font-size: 16px;
    color: var(--yellow);
  }
  .email {
    top: 445px;
    left: 387px;
    font-size: 16px;
  }
  .email-address { color: var(--yellow); }
  .slogan {
    top: 583px;
    left: 388px;
    font-size: 12px;
    letter-spacing: 0.8px;
    line-height: 16px;
    text-transform: uppercase;
    font-weight: 500;
  }
</style>
</head>
<body>
  <main class="canvas">
    <svg class="accent-bars" width="1200" height="848" viewBox="0 0 1200 848" aria-hidden="true">
      <g fill="var(--orange)">
        <rect x="580" y="252" width="5" height="21"/>
        <rect x="580" y="315" width="5" height="48"/>
        <rect x="580" y="380" width="5" height="15"/>
        <rect x="580" y="462" width="5" height="91"/>
      </g>
      <g fill="var(--grey)">
        <rect x="590" y="252" width="5" height="21"/>
        <rect x="590" y="315" width="5" height="48"/>
        <rect x="590" y="380" width="5" height="15"/>
        <rect x="590" y="462" width="5" height="91"/>
      </g>
      <line x1="587.5" y1="527" x2="587.5" y2="580" stroke="var(--grey)" stroke-width="1"/>
    </svg>

    <h1 class="line brand-name">R. Vandell</h1>
    <p class="line trade">Custom Tile &amp; Marble</p>
    <p class="line motto">"4 generations of Service"</p>
    <p class="line established">in business since 1975</p>
    <p class="line phone">555-284-7160</p>
    <p class="line website">www.vandelltile.example</p>
    <p class="line email">email:<span class="email-address">rkhome19@mailbox.example</span></p>
    <p class="line slogan">Creating<br>the most beautiful living spaces</p>
  </main>
</body>
</html>
```